Etiketten für  Beauty Vitaminreihe
Etiketten für Beauty Vitaminreihe
Zielgruppe
Wir sind eine Lifestyle Firma in Israel die Vitamine für die innere Schönheit produzieren. Unsere Zielgruppe sind Frauen mittleren Alters die sehr auf Ihr Äußeres wert legen.
Aufgabenstellung
Es sind 5 Arten von Vitamin Gummibärchen für die folgenden Vorteile sorgen:
1. Hair Skin and Nails Vitamine ( mit Biotin)
2. Kollagen (anti aging booster)
3. Multivitamin für Frauen
4. Multivitamin für Männer
5. Kurkuma und Ingwer
Genaue Aufteilung des Stickers und was draufstehen muss, wird in einem Word Dokument angehängt. Jede Art hat eine andere Farbe des Deckels, diese werden auch angehängt als Fotos.
Die Rückseite des Etiketts wird mit dem Gewinner fertiggestellt.
Das Design soll sehr simpel und minimalistisch und luxuriös sein, mit einem Hauch von Hotstamping Gold (Rahmen des Logos) und vielleicht noch ein weiteres kleines goldenes Detail.
Die Farben jedes Stickers sollte eine Pastellfarbe haben, in der Farbe des Deckels. Die Farben sollten sehr leicht und hell sein.
Die Maße der Flasche sind: Umfang 20 cm und Höhe 9 cm (von Ecke zu Ecke).
Ich hänge weitere Designs zur Inspiration an, die mir gefallen.

```html
<!DOCTYPE html>
<html lang="en">
<head>
<meta charset="utf-8">
<title>Silven Concentrated Biotin – Label</title>
<link rel="stylesheet" href="https://fonts.googleapis.com/css2?family=Jost:wght@300;400&display=swap">
<style>
  :root {
    --page: #e6e6e8;
    --label: #f8f8f9;
    --lavender: #9c98bd;
    --gold: #d8aa2a;
    --gold-soft: #f1e3b8;
  }
  * { margin: 0; padding: 0; box-sizing: border-box; }
  html, body { width: 1200px; height: 1147px; overflow: hidden; background: var(--page); }
  .canvas { position: relative; width: 1200px; height: 1147px; }

  .label {
    position: absolute; left: 321px; top: 73px;
    width: 559px; height: 1000px;
    background: var(--label);
    font-family: "Jost", sans-serif;
    overflow: hidden;
  }
  .wave-band {
    position: absolute; left: 0; top: 0; width: 100%; height: 206px;
    background: linear-gradient(160deg, #efeef6 0%, #e7e5f1 50%, #f1f0f7 100%);
  }
  .brand-name {
    position: absolute; left: 0; top: 118px; width: 100%;
    text-align: center;
    color: var(--lavender);
    font-family: "Jost", sans-serif;
    font-weight: 400; font-size: 40px; line-height: 48px;
    letter-spacing: 0.3em; padding-left: 0.3em;
  }
  .product-name {
    position: absolute; left: -228px; top: 570px;
    width: 575px; height: 94px;
    transform: rotate(-90deg);
    color: var(--lavender);
    font-weight: 300; font-size: 124px; line-height: 94px;
    letter-spacing: 0.21em; white-space: nowrap; text-align: center;
  }
  .product-type {
    position: absolute; left: 157px; top: 327px;
    color: var(--gold); font-size: 31px; line-height: 38px;
    letter-spacing: 0.2em; font-weight: 400;
  }
  .benefit-rule-h { position: absolute; left: 157px; top: 440px; width: 362px; height: 2px; background: var(--lavender); }
  .benefit-rule-v { position: absolute; left: 157px; top: 440px; width: 2px; height: 167px; background: var(--lavender); }
  .benefits {
    position: absolute; left: 192px; top: 486px; list-style: none;
    color: var(--lavender); font-size: 33px; line-height: 38px; letter-spacing: 0.13em;
  }
  .lotus-art {
    position: absolute; left: 200px; top: 634px; width: 313px; height: 132px;
    background: radial-gradient(ellipse at 50% 70%, #fbf6e8 0%, var(--gold-soft) 55%, rgba(216,170,42,0.15) 80%, transparent 100%);
    border-radius: 50% 50% 40% 40%;
  }
  .badge { position: absolute; top: 812px; width: 100px; height: 100px; }
  .badge-count { left: 240px; }
  .badge-sugar { left: 370px; }
  .badge text { font-family: "Jost", sans-serif; fill: var(--lavender); }
</style>
</head>
<body>
<main class="canvas">
  <section class="label">
    <div class="wave-band" role="img" aria-label="Fine lavender wavy line pattern"></div>
    <p class="brand-name">ORENA</p>

    <h1 class="product-name">SILVEN</h1>
    <p class="product-type">CONCENTRATED<br>BIOTIN</p>

    <div class="benefit-rule-h"></div>
    <div class="benefit-rule-v"></div>
    <ul class="benefits">
      <li>HEALTHY HAIR</li>
      <li>GLOWING SKIN</li>
      <li>STRONG NAILS</li>
    </ul>

    <div class="lotus-art" role="img" aria-label="Gold stippled lotus flower illustration"></div>

    <svg class="badge badge-count" viewBox="0 0 100 100" aria-label="70 gummies">
      <defs><path id="arc-count" d="M12,48 A38,38 0 0 0 88,48"/></defs>
      <path d="M8,52 A42,42 0 0 1 92,52" fill="none" stroke="var(--lavender)" stroke-width="1.6"/>
      <text x="50" y="46" text-anchor="middle" font-size="26">70</text>
      <text font-size="13" letter-spacing="2"><textPath href="#arc-count" startOffset="50%" text-anchor="middle">GUMMIES</textPath></text>
    </svg>

    <svg class="badge badge-sugar" viewBox="0 0 100 100" aria-label="Sugar free">
      <defs><path id="arc-sugar" d="M10,48 A40,40 0 0 0 90,48"/></defs>
      <path d="M8,52 A42,42 0 0 1 92,52" fill="none" stroke="var(--lavender)" stroke-width="1.6"/>
      <path d="M38,26 L50,20 L62,26 L62,40 L50,46 L38,40 Z M38,26 L50,32 L62,26 M50,32 L50,46" fill="none" stroke="var(--lavender)" stroke-width="1.6"/>
      <line x1="34" y1="16" x2="66" y2="50" stroke="var(--lavender)" stroke-width="1.6"/>
      <text font-size="13" letter-spacing="1.5"><textPath href="#arc-sugar" startOffset="50%" text-anchor="middle">SUGAR FREE</textPath></text>
    </svg>
  </section>
</main>
</body>
</html>
```